Saving Lives with Dental Sleep Medicine

Looking for a brochure to market Dental Sleep Medicine educational courses . Whoever wins this bid will be hired to design the rest of our marketing campaign.
Design should be clean, simple with a modern feel. Not busy. Our courses utilize the most modern technology available.
Brochure content is attached, if you can't fit it all that is ok, we can tweak the content later. We are more focused on the look and feel of this design.
This brochure is marketing a 2 day course so there needs to be a spot for date, location, time & cost. As well as a notice of where to register VelmoraLearning.com, info@velmoralearning.com or call 1.800.###.#### and registration fees.
Also need a spot for Dr. Pellingwood's bio (attached). It's too long so just leave as much space as you can and we can amend the content.
Thank you so much. Looking forward to your designs. VelmoLe Team :-)
Updates
Hello,
We are hoping for a minimalist design. Not busy. Clean and simple. We can reduce and minimize verbiage as needed. Just looking for layout and design.
Target Market(s)
Dentists
Requirements
Must have
- Clean lines, simple feel, minimalist and modern. Same font as logo. Black, white, gray.
Should not have
- Busy look and feel

```html
<!DOCTYPE html>
<html lang="en">
<head>
<meta charset="utf-8">
<title>Sleep &amp; Airway Management in a Dental Clinic</title>
<link href="https://fonts.googleapis.com/css2?family=Questrial&family=Roboto+Condensed:wght@400;700&display=swap" rel="stylesheet">
<style>
:root{
  --red:#e8505b;
  --ink:#2b2c2f;
  --dark:#4b4c50;
  --mid:#8d8e92;
  --soft:#d7d8da;
  --pale:#ececed;
  --white:#ffffff;
  --stage:#e3e3e4;
}
*{margin:0;padding:0;box-sizing:border-box}
html,body{width:1200px;height:732px;overflow:hidden;background:var(--stage)}
.page{position:absolute;top:38px;width:612px;height:791px;transform:scale(.815);transform-origin:0 0;background:var(--white);overflow:hidden;box-shadow:0 6px 18px rgba(0,0,0,.25);font-family:"Roboto Condensed",sans-serif;color:var(--ink)}
.page--front{left:85px}
.page--back{left:628px}
.abs{position:absolute}
.brand{display:flex;align-items:center;gap:10px;font-family:"Questrial",sans-serif;font-size:29px;color:var(--mid)}
.brand__mark{width:32px;height:32px;background:var(--red)}
.title{font-family:"Questrial",sans-serif;color:var(--red);font-size:17.5px;line-height:1.32;letter-spacing:.2px}
.tab{background:var(--mid);color:var(--white);font-family:"Questrial",sans-serif;font-size:14px;padding:8px 20px;clip-path:polygon(0 0,92% 0,100% 100%,0 100%)}
ul.list{list-style:none;font-size:9.6px;line-height:13.2px}
ul.list li::before{content:"• "}
.photo{background:linear-gradient(135deg,#9a9288,#5b5c63 55%,#2f3442)}
.footer{left:0;top:750px;width:612px;height:41px;background:#3a3b3e}
.footer__lead{position:absolute;left:0;top:0;height:41px;width:445px;background:var(--mid);clip-path:polygon(0 0,94% 0,100% 100%,0 100%);display:flex;align-items:center;padding-left:22px;gap:10px;color:var(--white);font-family:"Questrial",sans-serif;font-size:11.5px;font-weight:700}
.footer__social{position:absolute;right:14px;top:11px;display:flex;gap:8px}
.footer__social span{width:18px;height:18px;border:1.5px solid var(--white);border-radius:50%}
.desc{font-size:9.6px;line-height:13px;text-align:justify;color:#444}
.desc p+p{margin-top:13px}
.bio{font-size:8.1px;line-height:10.9px;text-align:justify;color:#444}
.bio p+p{margin-top:10px}
</style>
</head>
<body>

<!-- Front page -->
<section class="page page--front">
  <div class="abs photo" role="img" aria-label="Group of dentists observing a hands-on demonstration at a dental chair" style="left:250px;top:20px;width:362px;height:326px;clip-path:polygon(12% 0,100% 0,100% 100%,0 100%,8% 70%,0 47%,5% 32%)"></div>
  <div class="abs" style="left:0;top:20px;width:310px;height:105px;background:var(--white);clip-path:polygon(0 0,100% 0,92% 100%,0 100%)"></div>
  <div class="abs brand" style="left:24px;top:52px"><span class="brand__mark"></span>VelmoraLearning</div>
  <div class="abs" style="left:0;top:125px;width:300px;height:30px;background:var(--dark)"></div>
  <div class="abs" style="left:0;top:155px;width:310px;height:95px;background:var(--white);clip-path:polygon(0 0,90% 0,100% 100%,0 100%)"></div>
  <h1 class="abs title" style="left:24px;top:178px">SLEEP &amp; AIRWAY MANAGEMENT<br>IN A DENTAL CLINIC</h1>
  <div class="abs" style="left:0;top:250px;width:320px;height:96px;background:var(--dark);clip-path:polygon(0 0,100% 0,86% 100%,0 100%)"></div>
  <p class="abs" style="left:26px;top:268px;color:var(--white);font-family:'Questrial',sans-serif;font-size:14px;line-height:19px">NOCTA Plus System &amp; Fully<br>Digital Workflows for OAT</p>

  <div class="abs" style="left:0;top:346px;width:612px;height:404px;background:linear-gradient(#dcdcde,#f4f4f5 40%,#fafafa)"></div>
  <div class="abs tab" style="left:0;top:372px;width:232px">TOPICS COVERED:</div>
  <ul class="abs list" style="left:32px;top:411px;width:330px">
    <li>Fundamentals of Sleep &amp; Sleep Disorders</li>
    <li>Understand Obstructive Sleep Apnea (OSA) &amp; Treatment Options</li>
    <li>How to Implement an effective Sleep Screening Protocol in a Dental Clinic</li>
    <li>Sleep Testing</li>
    <li>How to order an appliance for OAT</li>
    <li>Appliance Selection</li>
    <li>Importance of patient selection</li>
    <li>Overview of NOCTA Plus System</li>
    <li>Hands-on workshop for NOCTA Tray Fitting</li>
    <li>Hands-on workshop for Bite-Registration</li>
    <li>Technology &amp; Sleep</li>
    <li>Fully Digital Workflow for OAT</li>
    <li>NOCTA Plus Case Studies</li>
    <li>Medical Billing for OAT</li>
    <li>How to maximize the utilization of your NOCTA Plus at your clinic</li>
    <li>Simple and easy to follow clinical workflow</li>
  </ul>
  <div class="abs photo" role="img" aria-label="Seminar room with attendees seated at tables" style="left:20px;top:633px;width:162px;height:97px"></div>
  <div class="abs photo" role="img" aria-label="Presenter speaking to course attendees" style="left:187px;top:633px;width:163px;height:97px"></div>

  <div class="abs" style="left:365px;top:393px;width:247px;height:337px;background:var(--white)"></div>
  <h2 class="abs" style="left:375px;top:403px;color:var(--red);font-family:'Questrial',sans-serif;font-size:14px;font-weight:400">Course Description:</h2>
  <div class="abs desc" style="left:375px;top:430px;width:225px">
    <p>Dental Sleep Medicine (DSM) has been growing rapidly over the past decade. Despite such growth, Oral Appliance Therapy (OAT) could be challenging in terms of predictability and workflow efficiency, resulting in many clinicians being reluctant to incorporate “Sleep &amp; OAT” into their clinics. However, most of these challenges can now be addressed by utilizing available technologies in healthcare industry; resulting in improved and predictable clinical workflows, patient experience, quality of care and access to care.</p>
    <p>This program will review the importance of Sleep &amp; Airway Management in comprehensive inter-disciplinary treatment planning and how airway &amp; sleep disorders, if left untreated, could adversely impact the long-term prognosis of dental treatments. It will also provide a practical step-by-step guide for implementing a simple &amp; predictable “Sleep and Airway Management” program; utilizing easy to implement systems, improved patient communication &amp; education through Intraoral scanning, &amp; 3D imaging AND a fully digital workflow for OAT.</p>
  </div>

  <div class="abs footer">
    <div class="footer__lead">For more information please contact us
      <svg width="14" height="14" viewBox="0 0 14 14" aria-hidden="true"><circle cx="7" cy="7" r="6" fill="none" stroke="#fff" stroke-width="1.2"/><ellipse cx="7" cy="7" rx="2.6" ry="6" fill="none" stroke="#fff" stroke-width="1"/><line x1="1" y1="7" x2="13" y2="7" stroke="#fff" stroke-width="1"/></svg>
      www.velmoralearning.com</div>
    <div class="footer__social"><span></span><span></span></div>
  </div>
</section>

<!-- Back page -->
<section class="page page--back">
  <div class="abs" style="left:0;top:20px;width:612px;height:284px;background:linear-gradient(90deg,#f2f2f3,#e4e4e6 55%,#bfc0c4)"></div>
  <div class="abs photo" role="img" aria-label="Portrait of the course presenter in a suit gesturing while speaking" style="left:340px;top:20px;width:272px;height:284px;background:linear-gradient(160deg,#d5d6d9,#8a8c93 45%,#1f2740)"></div>
  <div class="abs" style="left:0;top:30px;width:318px;height:96px;background:var(--white);clip-path:polygon(0 0,92% 0,100% 100%,0 100%);box-shadow:0 2px 6px rgba(0,0,0,.2)"></div>
  <div class="abs brand" style="left:24px;top:64px"><span class="brand__mark"></span>VelmoraLearning</div>
  <h1 class="abs title" style="left:24px;top:178px;font-size:18.5px">SLEEP &amp; AIRWAY MANAGEMENT<br>IN A DENTAL CLINIC</h1>
  <p class="abs" style="left:26px;top:240px;font-size:12.5px;font-weight:700;color:var(--dark)">Dr. Alaric Pellingwood</p>

  <div class="abs" style="left:0;top:304px;width:612px;height:446px;background:var(--white)"></div>
  <div class="abs tab" style="left:0;top:313px;width:230px">LEARNING OBJECTIVES:</div>
  <ul class="abs list" style="left:27px;top:352px;width:570px;font-size:10px;line-height:18px">
    <li>Step by step instruction on how to systematically integrate sleep into your practice</li>
    <li>Why dental clinics should have a comprehensive understanding of sleep &amp; airway disorders, and educate their patients</li>
    <li>How to implement a sleep and airway management program in a dental clinic</li>
    <li>Overview of some of the latest technologies in dentistry and how each could be utilized in Dental Sleep Medicine (DSM)</li>
    <li>How to utilize your NOCTA Plus System effectively in your clinic</li>
    <li>Proper selection of oral appliances for OSA</li>
    <li>Medical Billing for OAT</li>
  </ul>

  <div class="abs" style="left:27px;top:485px;width:570px;height:260px;background:var(--pale)"></div>
  <h2 class="abs" style="left:40px;top:492px;color:var(--red);font-size:12px;font-weight:700">About Dr. Alaric Pellingwood</h2>
  <div class="abs bio" style="left:40px;top:516px;width:545px">
    <p>Dr. Pellingwood received his Doctor of Dental Surgery (DDS) Degree and Bachelor of Medical Sciences from the University of Northmere. He also earned fellowships from Global Society of Facial Aesthetics &amp; Westbrook Institute for Advanced Dental Studies. He then furthered his education and training by completing a Research Fellowship in the area of “Sleep and Dental Sleep Medicine” at Lindqvist University Hospital, Aarberg.</p>
    <p>Dr. Pellingwood is a general dentist who maintains a group of private practices in Ridgefield and Carvale with an interest in Dental Sleep Medicine and TMD Management. He is actively involved in clinical research in Dental Sleep Medicine and his research focuses on developing new technologies to improve treatment outcome predictability and patient selection in Oral Appliance Therapy for patients with OSA (i.e. Obstructive Sleep Apnea) and improving clinical workflow efficiencies, utilizing different digital technologies. He is the recipient of the “2012 &amp; 2015 Clinical Research Award” and “2015 Clinical Excellence Award” from the Continental Academy of Dental Sleep Medicine (CADSM). He has lectured at numerous meetings such as Continental Academy of Dental Sleep Medicine Annual Meeting, CADSM Annual Meeting, GAO (Global Association for Orthodontics) Annual Meeting, Interdisciplinary Nordic Dental Sleep Medicine Academy (INDSMA), Lowland Society of Dental Sleep Medicine Annual</p>
    <p>Meeting and many more Sleep meetings across North America and Europe.<br>He is the founder and director of Prairie Dental Sleep Medicine Study Club and the Clinical Director at The Quiet Night Clinic. He is also the Chief Dental Officer at Halvern Sleep Systems, the developer of “NOCTA TM” Technology. Dr. Pellingwood is a major advocate for the importance of an inter-disciplinary approach to Dental Sleep Medicine which focuses on the collaboration of Sleep Physicians, Sleep Dentists and other healthcare professionals. He has been treating OSA patients for many years and also has trained hundreds of dentists in Dental Sleep Medicine.</p>
  </div>

  <div class="abs footer">
    <div class="footer__lead">For more information please contact us
      <svg width="14" height="14" viewBox="0 0 14 14" aria-hidden="true"><circle cx="7" cy="7" r="6" fill="none" stroke="#fff" stroke-width="1.2"/><ellipse cx="7" cy="7" rx="2.6" ry="6" fill="none" stroke="#fff" stroke-width="1"/><line x1="1" y1="7" x2="13" y2="7" stroke="#fff" stroke-width="1"/></svg>
      www.velmoralearning.com</div>
    <div class="footer__social"><span></span><span></span></div>
  </div>
</section>

</body>
</html>
```